Bright Harbour Electrical Limited needs advertisement brochure

We require a brochure with details of the services we provide. We have just become the only approved installer for RVL products on the Isle of Man and want to feature their producst heavily in the brochure centre pages. We estimate it will be 8 pages of A5 and we would like it to be landscape please. We have all the required content as per the word doc attached and just need it to be made to look professional. It doesn't need to include all the attached pictures and only certain information from the RVL brochure needs to be included (i.e the first couple of pages of write up).
Front Page - Just the Bright Harbour main logo and pics of vans
Page 2 - About us and the logos for who we are approved by (Kelby Traders Guild etc)
Page 3 - Domestic Electrical Services as per the word doc attached (those pictures don't have to be used so if you find better ones please go ahead and use).
Page 4 & 5 (Centre Pages) RVL information. Please make it clear that we are the only approved installers of their products on the Isle of Man.
Page 6 & 7 - Commercial Services as per the word doc attached (again if you can find better pictures than the ones contained in the word doc then feel free to use).
Page 8 - Back page to contain all our contact information.

Target Market(s)

Domestic and commercial customers. A design install and maintain company. Facility maintenance, preventative maintenance, fire alarm and emergency lighting contracts, home automation and sound system. Project management.

Industry/Entity Type

Electrical

Requirements
Must have
• Must be professional and appeal to both domestic and commercial customers. Has to be "BRIGHT" "EARTHY GREEN GLOBAL FEEL" like our logo shows. "CREATIVE" design. Possible similarity to our letter headed paper with part of the green globe down one side of the brochure. Must use Carlos Sanz text which is the Varnel Quist text same as logo. Snazzy looking, eye catching, appealing. Everything you would want to get new business in the door.
Nice to have
• As above
Should not have
• Over the top tacky earthy look. After all we also wire houses that are run by horrible oil boilers (no option). Don't want to put all my egg in one basket kind of thing.

```html
<!DOCTYPE html>
<html lang="en">
<head>
<meta charset="utf-8">
<title>Bright Harbour Electrical – Brochure Spreads</title>
<link href="https://fonts.googleapis.com/css2?family=Open+Sans:wght@400;600;700&family=Oswald:wght@400;500&display=swap" rel="stylesheet">
<style>
:root{
  --green:#2dc21a;
  --green-dark:#1f9e12;
  --charcoal:#3d3d3d;
  --ink:#333;
  --muted:#555;
  --paper:#fff;
  --mist:#e6f7ee;
  --stage:#d9d9d9;
}
*{box-sizing:border-box;margin:0;padding:0}
html,body{width:1200px;height:1200px;overflow:hidden}
body{background:radial-gradient(ellipse at center,#f2f2f2 0%,#dadada 70%,#cfcfcf 100%);font-family:"Open Sans",Arial,sans-serif;color:var(--ink);position:relative}
.page-label{position:absolute;width:323px;text-align:center;font:600 21px/1 "Open Sans",Arial,sans-serif;color:#222}
.page{position:absolute;width:323px;height:228px;background:var(--paper);box-shadow:0 1px 4px rgba(0,0,0,.35);overflow:hidden}
.page .frame{position:absolute;inset:0;width:100%;height:100%}
.page > *:not(.frame){position:absolute}
.col-l{left:239px}.col-r{left:653px}
.row1{top:66px}.row2{top:344px}.row3{top:631px}.row4{top:919px}
.lab1{top:31px}.lab2{top:314px}.lab3{top:594px}.lab4{top:882px}

.brand{text-align:center;width:100%;left:0}
.brand-mark{display:block;margin:0 auto;border-radius:50%;background:var(--green)}
.brand-name{font:600 9px/1 "Open Sans",Arial,sans-serif;color:var(--charcoal);letter-spacing:.3px;margin-top:4px}
.brand-sub{font:400 4px/1 "Open Sans",Arial,sans-serif;color:var(--muted);margin-top:2px}

.photo{border-radius:1px}
.body-copy{font-size:4.1px;line-height:1.42;color:var(--ink);text-align:justify}
.sub-head{font:700 5px/1 "Open Sans",Arial,sans-serif;color:var(--green)}
.display{font-family:"Oswald",Arial Narrow,sans-serif;font-weight:500;line-height:1.05;letter-spacing:-.2px}

.about-title{left:0;width:100%;text-align:center;top:28px;font:700 14px/1 "Open Sans",sans-serif;color:var(--green)}
.about-title span{border-bottom:1px solid var(--green)}
.badge{height:16px;border-radius:2px}

.contact-box{border:1.2px solid var(--green);border-radius:6px;padding:6px 7px;display:flex;gap:8px;font-size:3.9px;line-height:1.45}
.contact-box b{color:var(--green)}

.url-pill{border:1.2px solid var(--green);border-radius:8px;font:600 5px/1 "Open Sans",sans-serif;text-align:center;padding:3px 0}
.social{display:flex;gap:7px}
.social i{display:block;width:12px;height:12px;border-radius:50%;background:var(--green)}
</style>
</head>
<body>

<!-- Labels -->
<div class="page-label col-l lab1">Page 1</div>
<div class="page-label col-r lab1">Page 2</div>
<div class="page-label col-l lab2">Page 3</div>
<div class="page-label col-r lab2">Page 4</div>
<div class="page-label col-l lab3">Page 5</div>
<div class="page-label col-r lab3">Page 6</div>
<div class="page-label col-l lab4">Page 7</div>
<div class="page-label col-r lab4">Page 8</div>

<!-- Page 1: cover -->
<section class="page col-l row1">
  <svg class="frame" viewBox="0 0 323 228" preserveAspectRatio="none">
    <polygon points="0,0 95,0 0,38" fill="#3d3d3d"/>
    <polygon points="75,0 323,0 323,40 170,16" fill="#2dc21a"/>
    <polygon points="0,196 225,228 0,228" fill="#2dc21a"/>
    <polygon points="205,228 323,198 323,228" fill="#3d3d3d"/>
  </svg>
  <div class="brand" style="top:26px">
    <span class="brand-mark" style="width:36px;height:36px"></span>
    <div class="brand-name">BRIGHTHARBOUR</div>
    <div class="brand-sub">Electrical Limited</div>
  </div>
  <div class="photo" role="img" aria-label="Photograph of two branded white and green company vans" style="left:18px;top:95px;width:172px;height:92px;background:linear-gradient(160deg,#e9ecee 0%,#c9cfd3 55%,#2dc21a 78%,#444 100%)"></div>
  <div class="photo" role="img" aria-label="Rear view of company van with creative electrical installations lettering" style="left:198px;top:92px;width:90px;height:95px;background:linear-gradient(180deg,#5a5f63 0%,#e3e6e8 30%,#c5cacd 80%,#3a3a3a 100%)"></div>
</section>

<!-- Page 2: about us -->
<section class="page col-r row1">
  <svg class="frame" viewBox="0 0 323 228" preserveAspectRatio="none">
    <defs><linearGradient id="mist2" x1="0" y1="0" x2="1" y2="0"><stop offset="0" stop-color="#fff"/><stop offset=".5" stop-color="#e3f6ec"/><stop offset="1" stop-color="#fff"/></linearGradient></defs>
    <path d="M0,10 C90,40 220,-5 323,22 L323,0 L0,0Z" fill="url(#mist2)"/>
    <polygon points="0,196 225,228 0,228" fill="#2dc21a"/>
    <polygon points="205,228 323,198 323,228" fill="#3d3d3d"/>
  </svg>
  <div class="about-title"><span>About Us</span></div>
  <p class="body-copy" style="left:20px;top:58px;width:290px;text-align:center">Established by Daniel Creer in 2011 Bright Harbour Electrical Limited offers first class electrical services across the Isle of Man. Our fully qualified, professional electricians are committed to providing outstanding customer service every time. We consult closely with our domestic, commercial, and industrial clients to provide clean, modern, energy efficient systems that meet all expectations. We specialise in data networking, security lighting, home automation systems, fire alarms, emergency lighting, maintenance and inspection services.</p>
  <div class="badge" style="left:24px;top:117px;width:42px;background:#e8572a"></div>
  <div class="badge" style="left:82px;top:117px;width:66px;background:#3a3a3a"></div>
  <div class="badge" style="left:165px;top:117px;width:22px;background:#7bbf2a"></div>
  <div class="badge" style="left:205px;top:115px;width:34px;height:20px;background:#2a5caa"></div>
  <div class="badge" style="left:256px;top:120px;width:42px;height:8px;background:#4aa3d8"></div>
  <div class="brand" style="top:151px">
    <span class="brand-mark" style="width:26px;height:26px"></span>
    <div class="brand-name" style="font-size:6.5px">BRIGHTHARBOUR</div>
    <div class="brand-sub" style="font-size:3px">Electrical Limited</div>
  </div>
</section>

<!-- Page 3: domestic -->
<section class="page col-l row2">
  <svg class="frame" viewBox="0 0 323 228" preserveAspectRatio="none">
    <path d="M0,8 C90,32 220,-4 323,18 L323,0 L0,0Z" fill="#e6f7ee"/>
    <polygon points="0,196 225,228 0,228" fill="#2dc21a"/>
    <polygon points="205,228 323,198 323,228" fill="#3d3d3d"/>
  </svg>
  <div class="sub-head" style="left:22px;top:19px">Domestic Electrical Services</div>
  <p class="body-copy" style="left:22px;top:31px;width:280px">Bright Harbour Electrical Limited are experts in all domestic electrical jobs. Our friendly and reliable electricians can carry out everything from full re-wiring to simply changing a light fitting. Our fully qualified electricians can personally undertake any electrical work you need and no job is too small. On top of our first class service, we offer quick response times, fair prices, and free impartial advice.</p>
  <div class="photo" role="img" aria-label="Close-up photograph of stripped copper electrical cables" style="left:23px;top:74px;width:124px;height:55px;border:1.5px solid #2dc21a;background:linear-gradient(120deg,#1b6fb5 0%,#4aa0e0 40%,#d48a5a 60%,#1b4f8a 100%)"></div>
  <div style="left:160px;top:74px;width:1px;height:115px;background:#ccc"></div>
  <div class="photo" role="img" aria-label="Photograph of a softly lit room with modern LED lighting" style="left:168px;top:74px;width:127px;height:55px;border:1.5px solid #2dc21a;background:linear-gradient(120deg,#6a3fa8 0%,#c07ad0 45%,#e9d6a6 70%,#7d5ab8 100%)"></div>
  <p class="body-copy" style="left:23px;top:150px;width:124px">It is important to keep the electrics in your home in good working order. We are able to give friendly advice on the maintenance and repair of your electrical system and can also undertake both complete or partial re-wiring tasks.</p>
  <p class="body-copy" style="left:168px;top:150px;width:127px">We have years of experience in designing and installing all different types of lighting, including LED lights. Give us a call today to arrange a free lighting consultation.</p>
</section>

<!-- Page 4: RVL centre left -->
<section class="page col-r row2">
  <svg class="frame" viewBox="0 0 323 228" preserveAspectRatio="none">
    <polygon points="0,196 225,228 0,228" fill="#2dc21a"/>
    <polygon points="205,228 323,198 323,228" fill="#3d3d3d"/>
  </svg>
  <div class="display" style="left:20px;top:22px;font-size:22px;color:var(--green)">RVL</div>
  <div style="left:20px;top:52px;font:600 4px/1 'Open Sans',sans-serif;color:var(--charcoal)">Norvane Group</div>
  <div class="display" style="left:83px;top:23px;font-size:13.5px;color:var(--green)">WE ARE THE ONLY APPROVED INSTALLERS</div>
  <div class="display" style="left:83px;top:41px;font-size:13.5px;color:var(--charcoal)">OF YOUR PRODUCTS ON THE ISLE OF MAN</div>
  <div class="display" style="left:20px;top:70px;font-size:5px;color:var(--green);font-weight:400">INNOVATIVE RENEWABLE HEATING SOLUTIONS</div>
  <p class="body-copy" style="left:20px;top:79px;width:283px">RVL is an international manufacturer of innovative renewable heating solutions. For over 90 years our ranges of high performance products have warmed homes effectively and efficiently. Our complete range of renewable products provides everything needed to upgrade any heating system to the most modern and efficient levels, these include air to water and ground source heat pumps, biomass, wood pellet and log gasification boilers, intelligent thermal stores and dedicated controls systems.</p>
  <div class="display" style="left:20px;top:128px;font-size:5px;color:var(--green);font-weight:400">PRODUCT OVERVIEW</div>
  <p class="body-copy" style="left:20px;top:137px;width:167px">The basis behind all of our product designs is that they are all flexible heating solutions. Marketed under 'The ThermaFlow' concept this allows multiple heat sources to be successfully integrated and future-proof any installation. At the heart of the ThermaFlow concept is the CoreHeat, our innovative, high performance thermal store incorporating intelligent control.</p>
  <div class="photo" role="img" aria-label="Illustration of a modern white house on green lawns under a blue sky" style="left:202px;top:120px;width:101px;height:48px;border:1.5px solid #2dc21a;background:linear-gradient(180deg,#9fc6e8 0%,#dfeaf2 50%,#8cc34a 75%,#5f9e2d 100%)"></div>
</section>

<!-- Page 5: RVL centre right -->
<section class="page col-l row3">
  <svg class="frame" viewBox="0 0 323 228" preserveAspectRatio="none">
    <polygon points="0,196 225,228 0,228" fill="#2dc21a"/>
    <polygon points="205,228 323,198 323,228" fill="#3d3d3d"/>
  </svg>
  <div class="display" style="left:20px;top:28px;font-size:16px;color:var(--green)">EFFICIENT HEATING THAT WON'T COST THE EARTH</div>
  <div class="photo" role="img" aria-label="Product photograph of two grey and silver heating boiler units" style="left:20px;top:60px;width:145px;height:120px;background:linear-gradient(90deg,#fff 0%,#8e9398 15%,#d8dbde 35%,#6d7276 48%,#fff 52%,#b9bdc1 60%,#e9ebed 80%,#fff 100%)"></div>
  <p class="body-copy" style="left:172px;top:66px;width:133px;font-weight:600">We at RVL are well aware of this increasing need for change, and with our product ranges available today and in development for tomorrow, we are ensuring that the right technology is available to meet the requirements of the UK customers both now and in the future.</p>
  <div class="contact-box" style="left:172px;top:120px;width:133px">
    <div><b>RVL Norvane Group</b><br>Unit 4 Fernleigh Park<br>Ashcombe<br>Worcestershire<br>WR7 2LT</div>
    <div><b>Tel:</b> 01905 000214<br><b>Fax:</b> 01905 000215<br><b>Email:</b> info@rvl-uk.com<br>www.rvl-uk.com</div>
  </div>
</section>

<!-- Page 6: commercial -->
<section class="page col-r row3">
  <svg class="frame" viewBox="0 0 323 228" preserveAspectRatio="none">
    <path d="M0,8 C90,30 220,-4 323,16 L323,0 L0,0Z" fill="#e6f7ee"/>
    <polygon points="0,196 225,228 0,228" fill="#2dc21a"/>
    <polygon points="205,228 323,198 323,228" fill="#3d3d3d"/>
  </svg>
  <div class="sub-head" style="left:22px;top:11px">COMMERCIAL ELECTRICAL SERVICES</div>
  <div class="photo" role="img" aria-label="Photograph of commercial electrical switchgear" style="left:22px;top:25px;width:45px;height:50px;border:1.2px solid #2dc21a;background:linear-gradient(90deg,#9aa2a6,#e8eaeb,#8a9296)"></div>
  <p class="body-copy" style="left:74px;top:24px;width:232px;font-size:3.8px">Our commercial electricians are perfectly suited to carry out any type of electrical work for your business. We understand that getting through all the building regulations can be tough, and are fully on hand to offer advice, and guide you through the process. Our commercial electricians have years of experience, and can ensure that your work is carried out on time and to budget. If you are moving offices, Bright Harbour Electrical can advise you on the best electrical system for your business, and handle the entire process for you, from design to installation, and even maintenance and repairs. Each of our electricians is Trade Skills Board qualified, to ensure that your workplace meets all the electrical health and safety standards.</p>
  <div class="photo" role="img" aria-label="Photograph of a green emergency exit sign" style="left:22px;top:82px;width:45px;height:28px;border:1.2px solid #2dc21a;background:linear-gradient(90deg,#0f5a1e,#2aa84a,#0f5a1e)"></div>
  <div class="sub-head" style="left:74px;top:83px;font-size:4.2px">EMERGENCY LIGHTING</div>
  <p class="body-copy" style="left:74px;top:89px;width:232px;font-size:3.8px">Emergency lighting is vital for a working environment to ensure the safety of your employees. We are able to expertly install and maintain these systems, and advise you on the best solution for your business.</p>
  <div class="photo" role="img" aria-label="Photograph of a red fire alarm call point" style="left:22px;top:115px;width:45px;height:48px;border:1.2px solid #2dc21a;background:linear-gradient(120deg,#7a0c0c,#d62a2a,#f0d5d5)"></div>
  <div class="sub-head" style="left:74px;top:116px;font-size:4.2px">FIRE ALARM MAINTENANCE</div>
  <p class="body-copy" style="left:74px;top:122px;width:232px;font-size:3.8px">All fire systems must be regularly tested and maintenance is essential as it will prolong the life of a system and discover any faults that may occur. A system that is not maintained cannot be guaranteed to protect life and property. The only reliable and measurable means of ensuring that your existing fire detection and warning system remains compliant and fully functional is to instigate a plan of regular routine maintenance and testing carried out by a competent person supplemented by weekly user tests.</p>
  <div class="photo" role="img" aria-label="Photograph of a bright modern office interior with new lighting" style="left:22px;top:168px;width:45px;height:27px;border:1.2px solid #2dc21a;background:linear-gradient(90deg,#c9b48a,#f4efe3,#b8a47c)"></div>
  <div class="sub-head" style="left:74px;top:169px;font-size:4.2px">NEW LIGHTING AND POWER SYSTEMS</div>
  <p class="body-copy" style="left:74px;top:175px;width:232px;font-size:3.8px">Our commercial electricians can design and install the perfect lighting and power system for your business, and are on hand to give you advice and support that you need.</p>
</section>

<!-- Page 7: commercial continued -->
<section class="page col-l row4">
  <svg class="frame" viewBox="0 0 323 228" preserveAspectRatio="none">
    <path d="M0,8 C90,30 220,-4 323,16 L323,0 L0,0Z" fill="#e6f7ee"/>
    <polygon points="0,196 225,228 0,228" fill="#2dc21a"/>
    <polygon points="205,228 323,198 323,228" fill="#3d3d3d"/>
  </svg>
  <div class="photo" role="img" aria-label="Photograph of a hand using a security alarm keypad" style="left:27px;top:25px;width:41px;height:33px;border:1.2px solid #2dc21a;background:linear-gradient(135deg,#cfd3d6,#f3f4f5,#9aa0a4)"></div>
  <div class="sub-head" style="left:77px;top:26px;font-size:4.2px">SECURITY ALARMS</div>
  <p class="body-copy" style="left:77px;top:32px;width:222px;font-size:3.8px">It's vital to keep your security system in good working order to reduce false alarms and to ensure that the alarm will be raised in the event of a break-in. A maintenance contract will ensure that your intruder alarm is inspected and tested regularly, and can often pre-empt issues with your alarm system which would otherwise require an emergency call-out.</p>
  <div class="sub-head" style="left:27px;top:66px;font-size:4.2px">ELECTRICAL TESTING</div>
  <p class="body-copy" style="left:27px;top:72px;width:235px;font-size:3.8px">We can carry out all electrical inspection and testing for your home or business. This is needed in order to ensure that a working or living environment is electrically safe from potential accidents. Our friendly and experienced electricians can help you, by ensuring that your employees and residents are safe from potential hazards. Not only is it vital to meet all health and safety regulations for legal reasons, but the tests will also give you complete peace of mind that your building is safe. There are many types of Electrical Inspection, and it can often be difficult to understand exactly what level of electrical testing you need. We are on hand to guide you and provide the advice that you need.</p>
  <p class="body-copy" style="left:27px;top:133px;width:235px;font-size:3.8px">It is important when having Electrical Inspections carried out on your property, that you employ a trustworthy and reliable company. The safety of our customers is our number one priority, which is why we always use best quality equipment in our testing process. We also carry out Portable Appliance Testing (PAT) for businesses, landlords and individuals to ensure that the electrical products you use on a daily basis are safe. For businesses, these annual tests are mandatory by law, however we also advise that testing is carried out on personal appliances.</p>
  <div class="photo" role="img" aria-label="Photograph of a handheld voltage tester with probes" style="left:267px;top:77px;width:33px;height:44px;border:1.2px solid #2dc21a;background:linear-gradient(180deg,#f2f2f2,#e0b020,#333)"></div>
  <div class="photo" role="img" aria-label="Photograph of a yellow portable appliance testing kit" style="left:267px;top:133px;width:33px;height:38px;border:1.2px solid #2dc21a;background:linear-gradient(135deg,#f5d21a,#c9a50d,#444)"></div>
</section>

<!-- Page 8: back cover -->
<section class="page col-r row4">
  <svg class="frame" viewBox="0 0 323 228" preserveAspectRatio="none">
    <polygon points="0,0 95,0 0,38" fill="#3d3d3d"/>
    <polygon points="75,0 323,0 323,40 170,16" fill="#2dc21a"/>
    <polygon points="0,196 225,228 0,228" fill="#2dc21a"/>
    <polygon points="205,228 323,198 323,228" fill="#3d3d3d"/>
  </svg>
  <div class="brand" style="top:36px">
    <span class="brand-mark" style="width:36px;height:36px"></span>
    <div class="brand-name">BRIGHTHARBOUR</div>
    <div class="brand-sub">Electrical Limited</div>
  </div>
  <div class="display" style="left:0;width:100%;text-align:center;top:112px;font-size:14px;color:var(--green)">CALL US AT <span style="color:var(--charcoal)">07624 550182</span></div>
  <div style="left:0;width:100%;text-align:center;top:132px;font-size:6px;color:var(--ink)">Mail:info@brightharbourelectrical.com</div>
  <div class="url-pill" style="left:100px;top:150px;width:123px">www.brightharbourelectrical.com</div>
  <div class="social" style="left:114px;top:171px">
    <i></i><i></i><i></i><i></i>
  </div>
</section>

</body>
</html>
```